Geschäftspapiere für Rechtsanwaltskanzlei
Zielgruppe
Rechtsanwaltskanzlei mit dem Spezialgebiet Urheber-/Medienrecht; Mandanten sind Urheber, insbesondere von Musik- und Filmwerken, sowie Unternehmen, deren Unternehmenszweck die Herstellung- und Verwertung vorstehender Werke ist (z.B. Verlage, Filmproduktionsunternehmen). Das Design soll seriös sein, dabei aber einen modernen Touch haben.
Aufgabenstellung
Das Design muss im schwarz-weiß Ausdruck gut lesbar sein.
Es sollen folgende Informationen enthalten sein
Rechtsanwaltskanzlei Brunsmann
Rechtsanwältin Helga Brunsmann, MBA
Wiesenhang 27
38112 Tintfeld
Helga.Brunsmann@ra-brunsmann.com
Tel: +491524718260

```html
<!DOCTYPE html>
<html lang="de">
<head>
<meta charset="utf-8">
<title>Briefbogen – Rechtsanwaltskanzlei Brunsmann</title>
<link href="https://fonts.googleapis.com/css2?family=Didact+Gothic&display=swap" rel="stylesheet">
<style>
  :root {
    --paper: #ffffff;
    --ink: #1a1a1a;
    --accent: #7a6a58;
    --frame: #8a8a8a;
    --mark-grey: #7f7f7f;
  }
  html, body {
    margin: 0;
    padding: 0;
    width: 863px;
    height: 1200px;
    overflow: hidden;
    background: var(--paper);
  }
  .letterhead {
    position: relative;
    width: 863px;
    height: 1200px;
    font-family: "Didact Gothic", sans-serif;
    color: var(--ink);
  }
  .sheet-frame {
    position: absolute;
    left: 38px; top: 43px;
    width: 787px; height: 1114px;
    border: 1px solid var(--frame);
    box-sizing: border-box;
  }
  .top-band {
    position: absolute;
    left: 38px; top: 43px;
    width: 533px; height: 11px;
    background: var(--accent);
  }
  .bottom-band {
    position: absolute;
    left: 571px; top: 1146px;
    width: 254px; height: 11px;
    background: var(--accent);
  }
  .column-rule {
    position: absolute;
    left: 571px;
    width: 1px;
    background: var(--frame);
  }
  .column-rule--top { top: 43px; height: 264px; }
  .column-rule--bottom { top: 1098px; height: 48px; }
  .fold-mark {
    position: absolute;
    left: 38px;
    width: 14px; height: 1px;
    background: var(--accent);
  }
  .fold-mark--upper { top: 437px; }
  .fold-mark--lower { top: 600px; }

  .brand-square {
    position: absolute;
    left: 154px; top: 90px;
    width: 62px; height: 62px;
    background: var(--mark-grey);
  }
  .brand-name,
  .brand-sub,
  .return-line,
  .line {
    position: absolute;
    margin: 0;
    line-height: 1;
    white-space: nowrap;
  }
  .brand-name {
    left: 256px; top: 94px;
    font-size: 32px;
    letter-spacing: 1px;
  }
  .brand-sub {
    left: 257px; top: 132px;
    font-size: 14px;
    letter-spacing: 0.4px;
  }
  .return-line {
    left: 149px; top: 222px;
    font-size: 8.5px;
  }
  .sidebar .line { left: 581px; }
  .firm-name { font-size: 18px; }
  .firm-sub { font-size: 12.5px; }
  .contact { font-size: 10.5px; }
  .bank { font-size: 10px; }
</style>
</head>
<body>
<div class="letterhead">
  <div class="sheet-frame"></div>
  <div class="top-band"></div>
  <div class="bottom-band"></div>
  <div class="column-rule column-rule--top"></div>
  <div class="column-rule column-rule--bottom"></div>
  <div class="fold-mark fold-mark--upper"></div>
  <div class="fold-mark fold-mark--lower"></div>

  <div class="brand-square"></div>
  <p class="brand-name">BRUNSMANN</p>
  <p class="brand-sub">Rechtsanwaltskanzlei</p>

  <p class="return-line">BRUNSMANN Rechtsanwaltskanzlei &nbsp;|&nbsp; Wiesenhang 27 &nbsp;|&nbsp; 38112 Tintfeld</p>

  <div class="sidebar">
    <p class="line firm-name" style="top:105px">BRUNSMANN</p>
    <p class="line firm-sub" style="top:128px">Rechtsanwaltskanzlei</p>

    <p class="line contact" style="top:160px">Helga Brunsmann</p>
    <p class="line contact" style="top:175px">Rechtsanwältin, MBA</p>
    <p class="line contact" style="top:208px">Wiesenhang 27</p>
    <p class="line contact" style="top:222px">38112 Tintfeld</p>
    <p class="line contact" style="top:241px">Tel. +49 152 4718260</p>
    <p class="line contact" style="top:260px">E-Mail: Helga.Brunsmann@ra-brunsmann.com</p>

    <p class="line bank" style="top:1103px">Spreetal Bank Tintfeld</p>
    <p class="line bank" style="top:1116px">BIC: SPRTDEB1XXX</p>
    <p class="line bank" style="top:1129px">IBAN: DE12 3456 7800 1234 5678 90</p>
  </div>
</div>
</body>
</html>
```